Cover for Inspirational Daily Journal

This is the cover for a daily journal that will focus on inspirational content for black women. The cover should have a picture or silhouette of a black woman with a crown. The title is: "Grace in Bloom: A Year of Bright Mornings." The back won't have any words. Also the journal will be published on Pagewick.

```html
<!DOCTYPE html>
<html lang="en">
<head>
<meta charset="utf-8">
<title>Grace in Bloom: A Year of Bright Mornings — Cover</title>
<link rel="stylesheet" href="https://fonts.googleapis.com/css2?family=Oswald:wght@500;700&display=swap">
<style>
  :root {
    --page-bg: #ffffff;
    --teal-light: #1f6a76;
    --teal-mid: #14505a;
    --teal-deep: #0c3138;
    --ink: #0a0c0d;
    --silhouette: #060808;
    --gold-light: #e2c35a;
    --gold: #c9a22f;
    --gold-deep: #8f6f17;
    --silver: #b9bcbd;
  }
  * { margin: 0; padding: 0; box-sizing: border-box; }
  html, body {
    width: 1200px;
    height: 1200px;
    overflow: hidden;
    background: var(--page-bg);
  }
  .canvas {
    position: relative;
    width: 1200px;
    height: 1200px;
    display: flex;
    align-items: center;
    justify-content: center;
  }
  .cover {
    position: relative;
    width: 780px;
    height: 1080px;
    overflow: hidden;
    box-shadow: 0 18px 40px rgba(0, 0, 0, 0.18);
  }
  .cover-sky {
    position: absolute;
    inset: 0;
    background:
      radial-gradient(ellipse 60% 45% at 80% 28%, var(--teal-light) 0%, rgba(31, 106, 118, 0) 75%),
      linear-gradient(185deg, var(--teal-mid) 0%, var(--teal-deep) 55%, #0b2228 100%);
  }
  .cover-portrait {
    position: absolute;
    left: 0;
    top: 170px;
    width: 560px;
    bottom: 0;
    border-top-right-radius: 280px 360px;
    background: linear-gradient(90deg, var(--silhouette) 0%, #080a0b 70%, #0c1416 100%);
  }
  .cover-shade {
    position: absolute;
    left: 0;
    right: 0;
    bottom: 0;
    height: 240px;
    background: linear-gradient(180deg, rgba(10, 12, 13, 0) 0%, var(--ink) 80%);
  }
  .title-block {
    position: absolute;
    right: 48px;
    top: 500px;
    font-family: "Oswald", "Arial Narrow", sans-serif;
    text-transform: uppercase;
  }
  .title {
    font-weight: 700;
    font-size: 150px;
    line-height: 0.9;
    letter-spacing: -2px;
    background: linear-gradient(180deg, var(--gold-light) 0%, var(--gold) 55%, var(--gold-deep) 100%);
    -webkit-background-clip: text;
    background-clip: text;
    color: transparent;
  }
  .title-line { display: block; }
  .title-line--first { padding-left: 90px; }
  .subtitle {
    margin-top: 6px;
    font-weight: 500;
    font-size: 34px;
    letter-spacing: 0.5px;
    color: var(--silver);
    text-align: right;
  }
</style>
</head>
<body>
  <main class="canvas">
    <article class="cover">
      <div class="cover-sky" role="img" aria-label="Photograph background: dusky teal evening sky with a distant church spire"></div>
      <div class="cover-portrait" role="img" aria-label="Photograph: dark silhouette of a Black woman in profile, head raised, wearing an ornate crown"></div>
      <div class="cover-shade"></div>
      <div class="title-block">
        <h1 class="title">
          <span class="title-line title-line--first">Grace in</span>
          <span class="title-line">Bloom</span>
        </h1>
        <p class="subtitle">A Year of Bright Mornings</p>
      </div>
    </article>
  </main>
</body>
</html>
```